KAVELUXE Consultancy Business Card

We need a business card design for a new Image & Etiquette Consultancy Company.

The design should reflect the corporate colour found in the logo attached.

Info to include:

Name: Marelda Quon
Title: Image Consultant
Company: KA VELUXE CONSULTANCY
Address: 27 Pelham Street, #14-08 Harbourview Tower, Singapore 048215
Contact: 9317 6408
Email: marelda@kaveluxe.com.sg
Website: www.kaveluxe.com.sg

Industry/Entity Type

Business

```html
<!DOCTYPE html>
<html lang="en">
<head>
<meta charset="utf-8">
<title>KA VELUXE Consultancy – Business Card</title>
<link rel="stylesheet" href="https://fonts.googleapis.com/css2?family=Questrial&family=Open+Sans:wght@400;600;700&display=swap">
<style>
  :root {
    --purple-deep: #2a0f45;
    --purple-mid: #4a1d74;
    --purple-glow: #5b2a8a;
    --gold: #e9b924;
    --white: #ffffff;
    --ink: #3a1a5c;
    --backdrop: #ece8ef;
  }
  * { box-sizing: border-box; margin: 0; padding: 0; }
  html, body { width: 1200px; height: 900px; overflow: hidden; }
  body {
    background: var(--backdrop);
    font-family: "Open Sans", sans-serif;
    display: flex;
    flex-direction: column;
    align-items: center;
    justify-content: center;
    gap: 44px;
  }
  .card {
    width: 700px;
    height: 400px;
    border-radius: 14px;
    overflow: hidden;
    box-shadow: 0 14px 30px rgba(40, 15, 70, 0.22);
    position: relative;
  }
  /* Front */
  .card-front {
    background: radial-gradient(ellipse at 50% 35%, var(--purple-glow) 0%, var(--purple-mid) 35%, var(--purple-deep) 100%);
    display: flex;
    align-items: center;
    justify-content: center;
  }
  .brand-name {
    font-family: "Questrial", sans-serif;
    font-weight: 400;
    letter-spacing: 4px;
    white-space: nowrap;
  }
  .card-front .brand-name { color: var(--white); font-size: 40px; }
  /* Back */
  .card-back { display: flex; }
  .back-brand {
    width: 52%;
    background: var(--white);
    display: flex;
    align-items: center;
    justify-content: center;
  }
  .card-back .brand-name { color: var(--ink); font-size: 22px; letter-spacing: 2px; }
  .back-info {
    width: 48%;
    background: linear-gradient(160deg, var(--purple-mid) 0%, var(--purple-deep) 100%);
    color: var(--white);
    padding: 38px 26px 30px 22px;
    display: flex;
    flex-direction: column;
    position: relative;
  }
  .accent-triangle { position: absolute; left: -34px; top: 34px; }
  .person-name { color: var(--gold); font-weight: 700; font-size: 22px; line-height: 1.1; }
  .person-title { font-size: 14px; margin-top: 2px; }
  .address { font-size: 14px; line-height: 1.5; margin-top: 48px; }
  .contact-list { list-style: none; margin-top: auto; font-size: 15px; }
  .contact-list li { display: flex; align-items: center; gap: 9px; line-height: 1.75; }
  .contact-list svg { flex: none; }
</style>
</head>
<body>
  <section class="card card-front" aria-label="Card front">
    <span class="brand-name">KA VELUXE CONSULTANCY</span>
  </section>

  <section class="card card-back" aria-label="Card back">
    <div class="back-brand">
      <span class="brand-name">KA VELUXE CONSULTANCY</span>
    </div>
    <div class="back-info">
      <svg class="accent-triangle" width="46" height="30" viewBox="0 0 46 30" aria-hidden="true">
        <polygon points="2,15 40,2 40,28" fill="none" stroke="var(--gold)" stroke-width="3"/>
      </svg>
      <h1 class="person-name">Marelda Quon</h1>
      <p class="person-title">Image Consultant</p>
      <p class="address">27 Pelham Street, #14-08 Harbourview Tower, Singapore 048215</p>
      <ul class="contact-list">
        <li>
          <svg width="12" height="16" viewBox="0 0 12 16" aria-hidden="true"><rect x="1" y="1" width="10" height="14" rx="2" fill="none" stroke="var(--gold)" stroke-width="1.6"/><circle cx="6" cy="12.3" r="0.9" fill="var(--gold)"/></svg>
          9317 6408
        </li>
        <li>
          <svg width="14" height="11" viewBox="0 0 14 11" aria-hidden="true"><rect x="0.5" y="0.5" width="13" height="10" rx="1" fill="var(--gold)"/><polyline points="1,1 7,6 13,1" fill="none" stroke="var(--purple-deep)" stroke-width="1.2"/></svg>
          marelda@kaveluxe.com.sg
        </li>
        <li>
          <svg width="14" height="14" viewBox="0 0 14 14" aria-hidden="true"><circle cx="7" cy="7" r="6.2" fill="var(--gold)"/><g fill="none" stroke="var(--purple-deep)" stroke-width="0.9"><ellipse cx="7" cy="7" rx="2.6" ry="6.2"/><line x1="0.8" y1="7" x2="13.2" y2="7"/></g></svg>
          www.kaveluxe.com.sg
        </li>
      </ul>
    </div>
  </section>
</body>
</html>
```